Vocational Mentor needs an impressive business card

1. I need a business card (or maybe three with identic look) to promote me and my three business titles/services:
- Vocational Mentor. I help people find their vocation and live happily from it. I use my 20 years of experience in business, management and psychology to help them identify the most efficient ways to make a living doing what they are passionate about.
- Business Angel. I help founders start a succesful business with minimum risks and costs. I use my 20 years of experience in sales, management and entrepreneurship to help them identify the most efficient ways, in terms of time and cost, to validate their business idea.
- Learning Designer. I design unique learning programs that produce long-term cognitive and behavioural changes to people and organisations. I use my 20 years of experience in learning, teaching and change management to create minimalist experiences and processes that allow them to change efficiently in their pursued direction.

2. I would like a two-sided business card, on the front with my name, contact details and titles, on the back the explanation of the services.
Updates

Hi all,

I updated my brief, included contacts info and give feedback on all designs I got. I am new on this platform so please tell me if you need anything else or if I don't use corectly the platform forms.

Kind regards,
Tudor

Hi all,

I shortened the services description by deleting the phrase "I call..."

Kind regards,
Tudor

Target Market(s)

Freelancers, startups, people and organization willing to invest in change through ultimate learning experiences

Industry/Entity Type

Business

Font styles to use
Serif

Requirements
Must have
• Front side: full name, titles, web site, email, phone like below:
Tudor Vasilache
Vocational Mentor, Business Angel, Learning Designer
info@tudorvasilache.example
www.tudorvasilache.example
+40-745-TUDORV
Nice to have
• Back side: the description of the services I provide as in the task description.
1/3: it would be nice if I can jam all three titles on the front side but then I need a solution to jam all three services on the back side.

```html
<!DOCTYPE html>
<html lang="en">
<head>
<meta charset="utf-8">
<title>Tudor Vasilache – Vocational Mentor</title>
<link rel="stylesheet" href="https://fonts.googleapis.com/css2?family=Libre+Caslon+Text&display=swap">
<style>
  :root {
    --navy: #1f2163;
    --sheen: #ffffff;
    --accent: #ef8a3c;
    --rule: #d4562a;
    --ink-light: #ffffff;
    --edge: #3a3a3a;
    --page: #ffffff;
  }
  html, body {
    margin: 0;
    padding: 0;
    width: 726px;
    height: 1200px;
    overflow: hidden;
    background: var(--page);
  }
  .business-card {
    display: block;
    width: 726px;
    height: 1200px;
  }
  .card-face { fill: var(--navy); }
  .card-edge { fill: none; stroke: var(--edge); stroke-width: 2.5; }
  .sheen-stop-light { stop-color: var(--sheen); }
  .sheen-stop-mid { stop-color: #8e8fb5; }
  .sheen-stop-dark { stop-color: var(--navy); }
  .card-text { font-family: "Libre Caslon Text", "Times New Roman", serif; text-anchor: middle; }
  .holder-name { fill: var(--accent); font-size: 44px; letter-spacing: 0.5px; }
  .holder-title { fill: var(--ink-light); font-size: 36px; }
  .contact-line { fill: var(--ink-light); font-size: 36px; }
  .contact-rule { stroke: var(--rule); stroke-width: 2.5; }
</style>
</head>
<body>
<svg class="business-card" viewBox="0 0 726 1200" xmlns="http://www.w3.org/2000/svg">
  <defs>
    <clipPath id="card-shape">
      <path d="M97 2 H724 V1103 A95 95 0 0 1 629 1198 H2 V97 A95 95 0 0 1 97 2 Z"/>
    </clipPath>
    <linearGradient id="corner-sheen" gradientUnits="userSpaceOnUse" x1="80" y1="110" x2="420" y2="620">
      <stop offset="0" class="sheen-stop-light"/>
      <stop offset="0.45" class="sheen-stop-mid"/>
      <stop offset="1" class="sheen-stop-dark"/>
    </linearGradient>
  </defs>

  <g clip-path="url(#card-shape)">
    <rect class="card-face" x="0" y="0" width="726" height="1200"/>
    <path class="corner-sheen" fill="url(#corner-sheen)"
          d="M0 0 H714 C470 140, 250 520, 8 1200 H0 Z"/>
  </g>
  <path class="card-edge" d="M97 2 H724 V1103 A95 95 0 0 1 629 1198 H2 V97 A95 95 0 0 1 97 2 Z"/>

  <text class="card-text holder-name" x="367" y="370">TUDOR VASILACHE</text>
  <text class="card-text holder-title" x="367" y="432">Vocational Mentor</text>

  <line class="contact-rule" x1="65" y1="778" x2="688" y2="778"/>

  <text class="card-text contact-line" x="367" y="829">info@tudorvasilache.example</text>
  <text class="card-text contact-line" x="367" y="898">www.tudorvasilache.example</text>
  <text class="card-text contact-line" x="367" y="968">+40-745-TUDORV</text>
</svg>
</body>
</html>
```